Construction company focused on concrete and shed construction.

We need to update our current business card for brindlebuilds.com.au we would like an eye catching design with blue, grey and white incorporating our current logo.
Our company started off in concreting and due to varying factors we have expanded to include shed construction as well.
This has led to our current Logo looking a little out of place and somehow need to use the card to bring in the shed construction side of the business while not having to change current concrete look "BRINDLE" logo as we already have this incorporated into our company clothing and are not willing to change this yet.
Photo image attached for inspiration/ visual reference of type of work, not to be used on final design.
Please no cheesy designs of men in hard hats and tools
Final design should demonstrate a modern and service focused company.

Target Market(s)

Farmers, Business owners, Developers, Architects, Commercial project delivery

Industry/Entity Type

Construction Company

Contact Information for Business Card

Brindle Builds.
7c Harcourt st
South Launceston Tas
03 62918730

Font styles to use
Other font styles liked:
• see font in logo

Colors
3176b5
b2b2b2

Requirements
Must have
• Easy to read font,
• good contrast between back ground and writing
Nice to have
• Modern and corporate look with a fun but professional image.
Should not have
• Comic images or shadow images of tools/ people.

```html
<!DOCTYPE html>
<html lang="en">
<head>
<meta charset="utf-8">
<title>Brindle Builds – Business Card</title>
<link href="https://fonts.googleapis.com/css2?family=Roboto+Condensed:wght@400;700&display=swap" rel="stylesheet">
<style>
  :root {
    --brand-blue: #3176b5;
    --brand-grey: #b2b2b2;
    --text-grey: #6b6b6b;
    --card-white: #fbfbfb;
    --backdrop: #e9e6e1;
  }
  * { margin: 0; padding: 0; box-sizing: border-box; }
  html, body {
    width: 1200px; height: 911px; overflow: hidden;
    background: var(--backdrop);
    font-family: "Roboto Condensed", Arial, sans-serif;
  }
  .canvas {
    width: 1200px; height: 911px;
    display: flex; align-items: center; justify-content: center; gap: 40px;
  }
  .card {
    position: relative;
    width: 540px; height: 310px;
    background: var(--card-white);
    box-shadow: 0 6px 18px rgba(0,0,0,0.18);
  }
  .brand-mark {
    position: absolute;
    display: flex; align-items: center; gap: 10px;
    color: var(--brand-blue);
    font-weight: 700; font-size: 24px; letter-spacing: 1px;
  }
  .brand-mark__dot {
    width: 34px; height: 34px; border-radius: 50%;
    background: var(--brand-grey);
  }
  .card--front .brand-mark { top: 44px; right: 46px; }
  .contact {
    position: absolute; left: 46px; bottom: 36px;
    color: var(--text-grey); font-size: 15px; line-height: 1.3;
  }
  .contact__name {
    color: var(--brand-blue); font-weight: 700; font-size: 22px;
    line-height: 1.1;
  }
  .contact__title { font-size: 15px; margin-bottom: 10px; color: var(--text-grey); }
  .contact__address { margin-bottom: 8px; }
  .contact__row { display: flex; align-items: center; gap: 8px; }
  .contact__row svg { width: 13px; height: 13px; flex: none; }
  .card--back .brand-mark {
    top: 56px; left: 50%; transform: translateX(-50%);
  }
  .group-title {
    position: absolute; top: 140px; right: 40px; width: 300px;
    text-align: right;
    color: var(--brand-blue); font-weight: 700; font-size: 36px;
    letter-spacing: 1px; line-height: 1;
    padding: 8px 0;
    border-top: 2px solid var(--brand-grey);
    border-bottom: 2px solid var(--brand-grey);
  }
  .website {
    position: absolute; left: 40px; bottom: 36px;
    color: var(--text-grey); font-size: 15px;
  }
</style>
</head>
<body>
<main class="canvas">
  <section class="card card--front" aria-label="Card front">
    <div class="brand-mark"><span class="brand-mark__dot"></span><span>BRINDLE</span></div>
    <div class="contact">
      <p class="contact__name">LIAM CARTER</p>
      <p class="contact__title">CEO/FOUNDER</p>
      <p class="contact__address">Brindle Builds<br>7c Harcourt st<br>South Launceston Tas</p>
      <p class="contact__row">
        <svg viewBox="0 0 16 16" aria-hidden="true"><path fill="var(--brand-blue)" d="M3 1l3 3-1.5 2a9 9 0 0 0 5.5 5.5L12 10l3 3-2 2C7 15 1 9 1 3z"/></svg>
        03 62918730
      </p>
      <p class="contact__row">
        <svg viewBox="0 0 16 16" aria-hidden="true"><rect x="1" y="3" width="14" height="10" fill="var(--brand-blue)"/><path d="M1 3l7 6 7-6" stroke="#fff" stroke-width="1.4" fill="none"/></svg>
        info@brindlebuilds.com.au
      </p>
      <p class="contact__row">
        <svg viewBox="0 0 16 16" aria-hidden="true"><circle cx="8" cy="8" r="7" fill="var(--brand-blue)"/><path d="M1 8h14M8 1c-3 4-3 10 0 14M8 1c3 4 3 10 0 14" stroke="#fff" stroke-width="1" fill="none"/></svg>
        brindlebuilds.com.au
      </p>
    </div>
  </section>

  <section class="card card--back" aria-label="Card back">
    <div class="brand-mark"><span class="brand-mark__dot"></span><span>BRINDLE</span></div>
    <h1 class="group-title">BRINDLE GROUP</h1>
    <p class="website">www.brindlebuilds.com.au</p>
  </section>
</main>
</body>
</html>
```